Beautiful design for wordpress

I need a beautiful, colourful and feminine website. My business is called 'The Velvet Lantern', and I sell crystals, books, CD's, pendulums and other metaphysical items. I also provide Reiki (energy healing).
I want this design to be eye catching and inspire happiness and joy in those who see it. And I would love to see the use of the logo and its colours :)
Please add these on the web design: Home, About, Online store, Blog

Must have
• Colourful and playful, must use the logo somewhere, have the words on a menu saying 'Home, Blog, Online store and about' (or similar to those)And the design must stand out!
Should not have
• grey, brown and other boring colours.

```html
<!DOCTYPE html>
<html lang="en">
<head>
<meta charset="utf-8">
<title>The Velvet Lantern – Crystals &amp; Gifts</title>
<link rel="stylesheet" href="https://fonts.googleapis.com/css2?family=Open+Sans:ital,wght@0,400;0,600;0,700;1,400;1,600&display=swap">
<style>
:root{
  --pink:#ff3eb5;
  --pink-soft:#f7a8d8;
  --orange:#f9a94c;
  --ink:#1c1c1c;
  --text:#444;
  --muted:#888;
  --white:#fff;
  --green:#cbe07f;
  --band:#b9b6c4;
  --footer:#000;
  --line:#e4e4e4;
  --star:#e8214d;
}
*{box-sizing:border-box;margin:0;padding:0}
html,body{width:1200px;height:2261px;overflow:hidden}
body{font-family:"Open Sans",Arial,sans-serif;color:var(--text);background:var(--white);position:relative}
.wrap{width:938px;margin:0 auto;position:relative}
a{color:inherit;text-decoration:none}

.topbar{height:36px;background:var(--pink);color:var(--white);font-size:12px}
.topbar .wrap{display:flex;justify-content:space-between;align-items:center;height:36px}
.topbar-links{display:flex;gap:14px}
.topbar-links span.sep{opacity:.9}

.header{height:183px}
.header .wrap{height:183px}
.brand{position:absolute;left:0;top:48px;width:170px;display:flex;align-items:center;gap:10px}
.brand-mark{width:22px;height:22px;border-radius:50%;background:var(--pink);flex:none}
.brand-name{font-size:21px;font-weight:600;color:var(--ink);line-height:1.15}
.brand-tag{position:absolute;left:32px;top:104px;font-size:9px;font-weight:600;letter-spacing:1px;color:var(--text);text-transform:uppercase}
.perks{position:absolute;right:0;top:46px;display:flex;align-items:center;gap:14px}
.perk{display:flex;align-items:center;gap:10px}
.perk-icon{width:44px;height:44px;border-radius:50%;background:var(--orange);display:flex;align-items:center;justify-content:center}
.perk-title{font-size:13px;font-weight:600;color:var(--ink)}
.perk-sub{font-size:11px;color:var(--text)}
.bag{width:188px;height:44px;background:var(--orange);border-radius:3px;display:flex;align-items:center;gap:10px;padding:0 12px;color:var(--white);margin-left:6px}
.bag-title{font-size:13px;font-weight:600}
.bag-sub{font-size:10px}
.nav{position:absolute;left:371px;right:0;top:126px;height:41px;border-top:1px solid var(--line);display:flex;font-size:15px;color:var(--ink)}
.nav a{padding:14px 0 0;position:relative}
.nav a.active{color:var(--pink)}
.nav a.active::before{content:"";position:absolute;left:0;right:0;top:-4px;height:4px;background:var(--pink-soft)}
.nav a:nth-child(1){width:106px}
.nav a:nth-child(2){width:106px;text-align:center}
.nav a:nth-child(3){width:158px;text-align:center}
.nav a:nth-child(4){width:107px;text-align:center}
.nav a:nth-child(5){flex:1;text-align:right}

.hero{height:482px;position:relative;background:radial-gradient(ellipse 40% 60% at 60% 35%,#f1eef8 0%,#9c86c8 18%,#4b3681 45%,#1a1233 80%);overflow:hidden}
.hero-photo{position:absolute;inset:0}
.hero-text{position:absolute;left:128px;top:193px;color:var(--white)}
.hero-title{font-size:42px;font-weight:700;line-height:1.1}
.hero-sub{font-size:22px;font-style:italic;font-weight:600}
.hero-arrow{position:absolute;top:218px;color:#bbb;font-size:40px;line-height:1}
.hero-arrow.prev{left:10px}.hero-arrow.next{right:10px}
.dots{position:absolute;left:570px;top:453px;display:flex;gap:3px}
.dots i{width:13px;height:13px;border-radius:50%;background:#888;display:block}
.dots i.on{background:var(--white)}

.intro{height:336px}
.intro h2{position:absolute;left:0;top:48px;font-size:24px;font-weight:400;color:var(--ink)}
.intro p{position:absolute;left:0;top:100px;width:638px;font-size:11.5px;line-height:20.5px}
.intro-art{position:absolute;left:676px;top:23px;width:263px;height:256px;border-radius:50% 50% 40% 40%;background:radial-gradient(circle at 50% 45%,#e9dcf4 0%,#c9a8e0 35%,#f1b9d6 60%,#fff 75%)}

.healing{height:229px;background:linear-gradient(90deg,#b5b2c1 0%,#d6cfe0 40%,#e8dbe9 55%,#bdb9c8 100%);color:var(--white)}
.healing h2{position:absolute;left:0;top:34px;font-size:24px;font-weight:400}
.healing p{position:absolute;left:0;top:86px;width:938px;font-size:11.5px;line-height:20.5px;color:#fff}

.section-head{position:absolute;left:0;font-size:24px;font-weight:400;color:var(--ink)}
.pager{position:absolute;right:0;display:flex;gap:3px}
.pager i{width:21px;height:21px;border-radius:50%;background:#c9c9c9;display:flex;align-items:center;justify-content:center}

.sellers{height:535px}
.products{position:absolute;top:136px;left:0;width:938px;height:305px}
.card{position:absolute;top:0;width:195px;height:305px;background:var(--white);border:1px solid #ddd;box-shadow:0 2px 4px rgba(0,0,0,.18)}
.card-img{position:absolute;left:8px;top:8px;right:8px;height:163px}
.card-name{position:absolute;left:0;right:0;top:179px;height:59px;border-top:1px solid var(--line);border-bottom:1px solid var(--line);padding:17px 0 0 16px;font-size:17px;color:var(--ink)}
.stars{position:absolute;left:16px;top:246px;display:flex;gap:1px}
.price{position:absolute;left:16px;top:263px;font-size:22px;color:var(--ink)}
.card-icons{position:absolute;right:14px;top:244px;display:flex;flex-direction:column;gap:8px;align-items:center}

.blog{height:297px}
.posts{position:absolute;top:56px;left:0;width:938px;height:181px}
.post{position:absolute;top:0;width:455px;height:181px;background:var(--green)}
.post-img{position:absolute;left:0;top:0;width:170px;height:96px;background:linear-gradient(135deg,#6f5a34,#d9d2bd 50%,#8a6b3a)}
.post-meta{position:absolute;left:10px;top:120px;font-size:12px;font-style:italic;color:var(--ink);line-height:21px}
.post-title{position:absolute;left:188px;top:16px;font-size:14px;font-weight:600;color:var(--ink)}
.post-body{position:absolute;left:188px;top:56px;width:252px;font-size:11.5px;line-height:20.5px;text-align:justify;color:var(--ink)}

.footer{position:absolute;left:0;right:0;top:2098px;height:163px;background:var(--footer);color:var(--white)}
.footer-nav{position:absolute;left:0;top:42px;display:flex;gap:0;font-size:15px;font-weight:600}
.footer-nav a{margin-right:62px}
.cards-accepted{position:absolute;right:0;top:40px;display:flex;gap:3px}
.cards-accepted span{width:36px;height:24px;border-radius:2px;background:var(--white)}
.copyright{position:absolute;left:8px;top:102px;font-size:11px}
.social{position:absolute;right:0;top:98px;display:flex;gap:3px}
.social span{width:22px;height:22px;border-radius:50%;border:2px solid var(--white)}
</style>
</head>
<body>

<div class="topbar">
  <div class="wrap">
    <span>Welcome visitor you can login or create an account!</span>
    <nav class="topbar-links">
      <a href="#">My Account</a><span class="sep">|</span>
      <a href="#">Wishlist</a><span class="sep">|</span>
      <a href="#">Checkout</a><span class="sep">|</span>
      <a href="#">Search</a>
    </nav>
  </div>
</div>

<header class="header">
  <div class="wrap">
    <div class="brand">
      <span class="brand-mark"></span>
      <span class="brand-name">The Velvet<br>Lantern</span>
    </div>
    <div class="brand-tag">Crystals &amp; Gifts</div>

    <div class="perks">
      <div class="perk">
        <span class="perk-icon">
          <svg width="26" height="18" viewBox="0 0 26 18"><rect x="1" y="2" width="15" height="11" fill="#fff"/><path d="M16 6h5l4 4v3h-9z" fill="#fff"/><circle cx="6" cy="15" r="2.5" fill="#fff"/><circle cx="20" cy="15" r="2.5" fill="#fff"/></svg>
        </span>
        <div><div class="perk-title">Free Delivery</div><div class="perk-sub">for above $150</div></div>
      </div>
      <div class="perk">
        <span class="perk-icon">
          <svg width="24" height="24" viewBox="0 0 24 24" fill="none" stroke="#fff" stroke-width="3"><path d="M4 12a8 8 0 0 1 14-5"/><path d="M20 12a8 8 0 0 1-14 5"/><path d="M18 2v5h-5M6 22v-5h5" stroke-width="2.5"/></svg>
        </span>
        <div><div class="perk-title">Exchange &amp; Return</div><div class="perk-sub">within 2 weeks</div></div>
      </div>
      <a class="bag" href="#">
        <svg width="24" height="24" viewBox="0 0 24 24"><path d="M3 8h18l-2 14H5z" fill="#fff"/><path d="M8 8V6a4 4 0 0 1 8 0v2" fill="none" stroke="#fff" stroke-width="2"/></svg>
        <div><div class="bag-title">My Shopping Bag</div><div class="bag-sub">(0) Items - $ 0.00</div></div>
      </a>
    </div>

    <nav class="nav">
      <a href="#" class="active">Home</a>
      <a href="#">About</a>
      <a href="#">Online store</a>
      <a href="#">Blog</a>
      <a href="#">Contact us</a>
    </nav>
  </div>
</header>

<section class="hero">
  <div class="hero-photo" role="img" aria-label="Open hand holding a glowing white light against a starry purple galaxy"></div>
  <div class="hero-text">
    <div class="hero-title">Reiki</div>
    <div class="hero-sub">Give Light To Your Hands</div>
  </div>
  <span class="hero-arrow prev">&#10094;</span>
  <span class="hero-arrow next">&#10095;</span>
  <div class="dots"><i></i><i></i><i class="on"></i><i></i></div>
</section>

<section class="intro">
  <div class="wrap" style="height:336px">
    <h2>The Velvet Lantern</h2>
    <p>Lorem ipsum dolor sit amet, consectetur adipisicing elit, sed do eiusmod tempor incididunt ut labore et dolore magna aliqua. Ut enim ad minim veniam, quis nostrud exercitation ullamco laboris nisi ut aliquip ex ea commodo consequat. Duis aute irure dolor in reprehenderit in voluptate velit esse cillum dolore eu fugiat nulla pariatur. Excepteur sint occaecat cupidatat non proident, sunt in culpa qui officia deserunt mollit anim id est laborum. Lorem ipsum dolor sit amet, consectetur adipisicing elit, sed do eiusmod tempor incididunt ut labore et dolore magna aliqua. Ut enim ad minim veniam, quis nostrud exercitation ullamco laboris nisi ut aliquip ex ea commodo consequat. Duis aute irure dolor in reprehenderit in voluptate velit esse cillum dolore eu fugiat nulla pariatur. Excepteur sint occaecat cupidatat non proident, sunt in culpa qui officia deserunt mollit anim id est laborum</p>
    <div class="intro-art" role="img" aria-label="Meditating figure with glowing chakra points seated on a pink lotus"></div>
  </div>
</section>

<section class="healing" role="img" aria-label="Soft glowing open hand in pale lavender light">
  <div class="wrap" style="height:229px">
    <h2>Reiki Healing</h2>
    <p>Lorem ipsum dolor sit amet, consectetur adipisicing elit, sed do eiusmod tempor incididunt ut labore et dolore magna aliqua. Ut enim ad minim veniam, quis nostrud exercitation ullamco laboris nisi ut aliquip ex ea commodo consequat. Duis aute irure dolor in reprehenderit in voluptate velit esse cillum dolore eu fugiat nulla pariatur. Excepteur sint occaecat cupidatat non proident, sunt in culpa qui officia deserunt mollit anim id est laborum. Lorem ipsum dolor sit amet, consectetur adipisicing elit, sed do eiusmod tempor incididunt ut labore et dolore magna aliqua. Ut enim ad minim veniam, quis nostrud exercitation ullamco laboris nisi ut aliquip ex ea commodo consequat. Duis aute irure dolor in reprehenderit in voluptate velit esse cillum dolore eu fugiat nulla pariatur. Excepteur sint occaecat cupidatat non proident, sunt in culpa qui officia deserunt mollit anim id est laborum</p>
  </div>
</section>

<section class="sellers">
  <div class="wrap" style="height:535px">
    <h2 class="section-head" style="top:64px">Our Best Sellers</h2>
    <div class="pager" style="top:73px">
      <i><svg width="9" height="10" viewBox="0 0 9 10"><path d="M7 1L2 5l5 4" fill="none" stroke="#fff" stroke-width="2"/></svg></i>
      <i><svg width="9" height="10" viewBox="0 0 9 10"><path d="M2 1l5 4-5 4" fill="none" stroke="#fff" stroke-width="2"/></svg></i>
    </div>

    <div class="products">
      <article class="card" style="left:0">
        <div class="card-img" role="img" aria-label="Colourful gemstone prayer bead necklace with tassel" style="background:radial-gradient(circle at 50% 50%,#fff 30%,#f4e9e2 60%,#fff 80%)"></div>
        <div class="card-name">Mystical Charm</div>
        <div class="stars"><svg width="52" height="9" viewBox="0 0 52 9"><g fill="#e8214d"><circle cx="4" cy="4.5" r="3.5"/><circle cx="14" cy="4.5" r="3.5"/><circle cx="24" cy="4.5" r="3.5"/></g><g fill="#bbb"><circle cx="34" cy="4.5" r="3.5"/><circle cx="44" cy="4.5" r="3.5"/></g></svg></div>
        <div class="price">$63.00</div>
        <div class="card-icons">
          <svg width="18" height="16" viewBox="0 0 18 16"><path d="M9 15S1 10 1 5a4 4 0 0 1 8-1 4 4 0 0 1 8 1c0 5-8 10-8 10z" fill="none" stroke="#aaa" stroke-width="1.3"/></svg>
          <svg width="20" height="22" viewBox="0 0 20 22"><path d="M2 8h16l-1 13H3z" fill="#f9a94c"/><path d="M6 8V5a4 4 0 0 1 8 0v3" fill="none" stroke="#f9a94c" stroke-width="2"/></svg>
        </div>
      </article>

      <article class="card" style="left:253px">
        <div class="card-img" role="img" aria-label="Golden sun ornament" style="background:radial-gradient(circle,#d9a93a 0%,#b88625 35%,#efe2cc 55%,#e8dcc8 100%)"></div>
        <div class="card-name">Sun Pendent</div>
        <div class="stars"><svg width="52" height="9" viewBox="0 0 52 9"><g fill="#e8214d"><circle cx="4" cy="4.5" r="3.5"/><circle cx="14" cy="4.5" r="3.5"/><circle cx="24" cy="4.5" r="3.5"/></g><g fill="#bbb"><circle cx="34" cy="4.5" r="3.5"/><circle cx="44" cy="4.5" r="3.5"/></g></svg></div>
        <div class="price">$63.00</div>
        <div class="card-icons">
          <svg width="18" height="16" viewBox="0 0 18 16"><path d="M9 15S1 10 1 5a4 4 0 0 1 8-1 4 4 0 0 1 8 1c0 5-8 10-8 10z" fill="none" stroke="#aaa" stroke-width="1.3"/></svg>
          <svg width="20" height="22" viewBox="0 0 20 22"><path d="M2 8h16l-1 13H3z" fill="#f9a94c"/><path d="M6 8V5a4 4 0 0 1 8 0v3" fill="none" stroke="#f9a94c" stroke-width="2"/></svg>
        </div>
      </article>

      <article class="card" style="left:498px">
        <div class="card-img" role="img" aria-label="Audio CD set in a jewel case" style="background:radial-gradient(circle,#fff 6%,#c9d7f0 20%,#9fb4e2 45%,#555 70%,#3a3a3a 100%)"></div>
        <div class="card-name">CD Set</div>
        <div class="stars"><svg width="52" height="9" viewBox="0 0 52 9"><g fill="#e8214d"><circle cx="4" cy="4.5" r="3.5"/><circle cx="14" cy="4.5" r="3.5"/><circle cx="24" cy="4.5" r="3.5"/></g><g fill="#bbb"><circle cx="34" cy="4.5" r="3.5"/><circle cx="44" cy="4.5" r="3.5"/></g></svg></div>
        <div class="price">$63.00</div>
        <div class="card-icons">
          <svg width="18" height="16" viewBox="0 0 18 16"><path d="M9 15S1 10 1 5a4 4 0 0 1 8-1 4 4 0 0 1 8 1c0 5-8 10-8 10z" fill="none" stroke="#aaa" stroke-width="1.3"/></svg>
          <svg width="20" height="22" viewBox="0 0 20 22"><path d="M2 8h16l-1 13H3z" fill="#f9a94c"/><path d="M6 8V5a4 4 0 0 1 8 0v3" fill="none" stroke="#f9a94c" stroke-width="2"/></svg>
        </div>
      </article>

      <article class="card" style="left:743px">
        <div class="card-img" role="img" aria-label="Purple hardcover reference book" style="background:linear-gradient(180deg,#5a1f5c 0%,#6e2a6e 55%,#4a1b4c 100%)"></div>
        <div class="card-name">Bible Dictionary</div>
        <div class="stars"><svg width="52" height="9" viewBox="0 0 52 9"><g fill="#e8214d"><circle cx="4" cy="4.5" r="3.5"/><circle cx="14" cy="4.5" r="3.5"/><circle cx="24" cy="4.5" r="3.5"/></g><g fill="#bbb"><circle cx="34" cy="4.5" r="3.5"/><circle cx="44" cy="4.5" r="3.5"/></g></svg></div>
        <div class="price">$63.00</div>
        <div class="card-icons">
          <svg width="18" height="16" viewBox="0 0 18 16"><path d="M9 15S1 10 1 5a4 4 0 0 1 8-1 4 4 0 0 1 8 1c0 5-8 10-8 10z" fill="none" stroke="#aaa" stroke-width="1.3"/></svg>
          <svg width="20" height="22" viewBox="0 0 20 22"><path d="M2 8h16l-1 13H3z" fill="#f9a94c"/><path d="M6 8V5a4 4 0 0 1 8 0v3" fill="none" stroke="#f9a94c" stroke-width="2"/></svg>
        </div>
      </article>
    </div>
  </div>
</section>

<section class="blog">
  <div class="wrap" style="height:297px">
    <h2 class="section-head" style="top:0">Blog Updates</h2>
    <div class="pager" style="top:9px">
      <i><svg width="9" height="10" viewBox="0 0 9 10"><path d="M7 1L2 5l5 4" fill="none" stroke="#fff" stroke-width="2"/></svg></i>
      <i><svg width="9" height="10" viewBox="0 0 9 10"><path d="M2 1l5 4-5 4" fill="none" stroke="#fff" stroke-width="2"/></svg></i>
    </div>
    <div class="posts">
      <article class="post" style="left:0">
        <div class="post-img" role="img" aria-label="Crescent moon in a misty golden sky"></div>
        <div class="post-meta">Posted on 17/05/14<br>By Mara Ellison</div>
        <h3 class="post-title">Reiki Healing</h3>
        <p class="post-body">Lorem ipsum dolor sit amet, consectetur adipisicing elit, sed do eiusmod tempor incididunt ut labore et dolore magna aliqua. Ut enim ad minim veniam, quis nostrud exercitation ullamco</p>
      </article>
      <article class="post" style="left:483px">
        <div class="post-img" role="img" aria-label="Crescent moon in a misty golden sky"></div>
        <div class="post-meta">Posted on 17/05/14<br>By Mara Ellison</div>
        <h3 class="post-title">Reiki Healing</h3>
        <p class="post-body">Lorem ipsum dolor sit amet, consectetur adipisicing elit, sed do eiusmod tempor incididunt ut labore et dolore magna aliqua. Ut enim ad minim veniam, quis nostrud exercitation ullamco</p>
      </article>
    </div>
  </div>
</section>

<footer class="footer">
  <div class="wrap" style="height:163px">
    <nav class="footer-nav">
      <a href="#">Home</a>
      <a href="#">About</a>
      <a href="#">Online store</a>
      <a href="#">Blog</a>
      <a href="#">Contact us</a>
    </nav>
    <div class="cards-accepted" aria-label="Accepted payment methods">
      <span></span><span></span><span></span><span></span><span></span>
    </div>
    <div class="copyright">Copyright ©2014. All rights reserved.</div>
    <div class="social" aria-label="Social links">
      <span></span><span></span><span></span><span></span>
    </div>
  </div>
</footer>

</body>
</html>
```